Name card design for KOV mobile accessories company

KOV is an upmarket brand, we are looking for professional business card design.

the design should be neat and simple but giving a strong feeling.
should not be colorful. make it black/white/gray tone

Name:
Job title:
Contact no.:
company address: i would like the company address to be very small and thin.
link to social media profile:
company website:

*the company have no website yet
as the project is done please i also would like the font that use in design as well; for more further people in company need a business card:)
Updates

Thank you for all super fast submission :D they're all look cool!

i have just update my brief to make the statement clearer, please check it out :)
if you have any question please dont hesitate to ask.
i would like see more design from you! 
Keep it up!  :D

Target Market(s)

Company target are upmarket company distributor, such as Vordane and Pilto store.

Industry/Entity Type

Business

Font styles to use
Serif
Sans Serif
Other font styles liked:
• Formal and mordern

Colors
ffffff
eeeeee
d3d3d3
919191
474747
1b1b1b
000000
333333

Requirements
Must have
• The design must be professional clean and clear but also Strong and Modern!
text should be formal and mordern
Should not have
• No complicated design!

```html
<!DOCTYPE html>
<html lang="en">
<head>
<meta charset="utf-8">
<title>KOV business card</title>
<link href="https://fonts.googleapis.com/css2?family=Montserrat:wght@300;400;600;700&display=swap" rel="stylesheet">
<style>
  :root {
    --white: #ffffff;
    --paper: #eeeeee;
    --backdrop: #d3d3d3;
    --mid-gray: #919191;
    --dark-gray: #474747;
    --ink: #1b1b1b;
    --black: #000000;
    --charcoal: #333333;
  }
  * { box-sizing: border-box; margin: 0; padding: 0; }
  html, body {
    width: 1200px; height: 907px; overflow: hidden;
    background: var(--backdrop);
    font-family: "Montserrat", sans-serif;
  }
  .stage {
    position: relative; width: 1200px; height: 907px;
    display: flex; flex-direction: column; align-items: center; justify-content: center; gap: 60px;
  }
  .card {
    position: relative; width: 580px; height: 330px; overflow: hidden;
    box-shadow: 0 6px 18px rgba(0,0,0,0.18);
  }
  .card svg.band { position: absolute; inset: 0; width: 100%; height: 100%; }

  /* back */
  .card--back { background: var(--charcoal); }
  .brand {
    display: flex; align-items: center; gap: 12px;
    font-weight: 700; letter-spacing: 6px; line-height: 1;
  }
  .brand__square { width: 18px; height: 18px; }
  .card--back .brand {
    position: absolute; left: 50%; top: 118px; transform: translateX(-50%);
    color: var(--white); font-size: 64px;
  }
  .card--back .brand__square { background: var(--white); }
  .card--back .website {
    position: absolute; right: 26px; bottom: 22px;
    color: var(--white); font-size: 11px; font-weight: 400; letter-spacing: 0.5px;
  }

  /* front */
  .card--front { background: var(--white); color: var(--ink); }
  .card--front .brand {
    position: absolute; left: 44px; top: 40px;
    color: var(--ink); font-size: 48px;
  }
  .card--front .brand__square { background: var(--ink); }
  .details { position: absolute; left: 250px; top: 44px; }
  .person__name { font-size: 15px; font-weight: 600; letter-spacing: 1.5px; text-transform: uppercase; }
  .person__title { font-size: 12px; font-weight: 400; margin-top: 3px; }
  .address { font-size: 10px; font-weight: 300; line-height: 1.45; margin-top: 14px; color: var(--dark-gray); }
  .contacts { list-style: none; margin-top: 14px; font-size: 11px; font-weight: 400; }
  .contacts li { display: flex; align-items: center; gap: 8px; line-height: 1.6; }
  .contacts svg { width: 11px; height: 11px; fill: var(--ink); }
  .card--front .website {
    position: absolute; right: 30px; bottom: 26px;
    font-size: 12px; font-weight: 400;
  }
  .card--front .website strong { font-weight: 700; }
</style>
</head>
<body>
<main class="stage">

  <section class="card card--back" aria-label="Card back">
    <svg class="band" viewBox="0 0 580 330" preserveAspectRatio="none" aria-hidden="true">
      <path d="M0 330 L0 318 C180 300 400 260 580 200 L580 330 Z" fill="var(--dark-gray)"/>
      <path d="M0 318 C180 300 400 260 580 200 L580 210 C400 270 180 308 0 326 Z" fill="var(--white)"/>
    </svg>
    <div class="brand"><span class="brand__square"></span>KOV</div>
    <p class="website">www.kovaccessories.com</p>
  </section>

  <section class="card card--front" aria-label="Card front">
    <svg class="band" viewBox="0 0 580 330" preserveAspectRatio="none" aria-hidden="true">
      <path d="M0 190 C40 270 120 300 230 312 L580 318 L580 330 L0 330 Z" fill="var(--dark-gray)"/>
      <path d="M0 214 C50 285 130 306 240 316 L580 322 L580 330 L0 330 Z" fill="var(--charcoal)"/>
      <path d="M0 180 C42 262 122 292 232 304 L580 310 L580 313 L230 307 C118 296 38 266 0 188 Z" fill="var(--mid-gray)"/>
    </svg>
    <div class="brand"><span class="brand__square"></span>KOV</div>
    <div class="details">
      <p class="person__name">Elias Varn</p>
      <p class="person__title">Managing Director</p>
      <p class="address">27 Level 9 Harlow Court<br>Wexmoor Road</p>
      <ul class="contacts">
        <li><svg viewBox="0 0 12 12"><path d="M2 1h2l1 3-1.5 1a7 7 0 0 0 3.5 3.5L8 7l3 1v2a1 1 0 0 1-1 1A9 9 0 0 1 1 2a1 1 0 0 1 1-1z"/></svg>014 862 3570</li>
        <li><svg viewBox="0 0 12 12"><path d="M3.5 0h5a1 1 0 0 1 1 1v10a1 1 0 0 1-1 1h-5a1 1 0 0 1-1-1V1a1 1 0 0 1 1-1zm.5 1.5v8h4v-8z"/></svg>014 862 3571</li>
        <li><svg viewBox="0 0 12 12"><path d="M1 4h10v6H1zM3 1h6v3H3zM3 6h2v1H3z"/></svg>014 862 3572</li>
        <li><svg viewBox="0 0 12 12"><path d="M0 2h12v8H0zm1 1v.5l5 3 5-3V3z"/></svg>elias@kovmail.com</li>
      </ul>
    </div>
    <p class="website">www.<strong>kovaccessories</strong>.com</p>
  </section>

</main>
</body>
</html>
```